Top producing Realtors in Washington, D.C. need cover design for home buying book.

We need a cover design for our printed home buying booklet. Right now our working title is "Capital Area Property's Complete Handbook for Savvy Purchasers". The book guides readers through the homebuying process. The inside of the book is text, real images of homes, rooms, and probably some exterior shots of the Washington, D.C. area. We have a little professor cartoon icon we got from Pictavault.com that we are using inside the book when we have an important point to me made within the text. Think of how guides for beginners have that target with a dart on the bullseye. (We've attached an example of the icon.) We'd like the cover to be graphics that help illustrate the feeling of "smart" "intelligent" but not stuffy, since we do have a slightly cartoonish feel in parts of the inside with the professor icon. So we'd like to include real images of nice parts of a house--living room, kitchen, bathroom, but also a graphic aspect that's not real images. WE'RE OPEN TO OTHER IDEAS! but we just had those thoughts. We want to primarily get across to readers that they are smart--or we can help them be smart--about buying real estate, and this is the guide for them, and we can help them get a nice home.We have an account with pictavault.com and have license to use the attached photos and icon. After seeing some samples, we like the idea of the professor icon on the cover. We might have additional photos, please use pictavault.com and we can download then forward licensed images, so long as their not "editorial only" images. Also, Please include "By Marisa Vendrapolo and Jonathan Wexbrunel somewhere on the cover. Does not have to be prominent but must be there.

The dimensions of the book is is 5.5 inches wide and 8.5 inches long. We would like it to bleed off in all directions.

Target Market(s)

Home buyers

Font styles to use
Serif

Requirements
Must have
• We want to primarily get across to readers that they are smart--or we can help them be smart--about buying real estate, and this is the guide for them. Sophisticated, but not stuffy.

```html
<!DOCTYPE html>
<html lang="en">
<head>
<meta charset="utf-8">
<title>Capital Area Property's Complete Handbook for Savvy Purchasers — Cover</title>
<link rel="stylesheet" href="https://fonts.googleapis.com/css2?family=Bebas+Neue&family=Oswald:wght@200&display=swap">
<style>
  :root {
    --page: #f2f2f4;
    --cover-light: #fbfbfc;
    --cover-shade: #e8e8eb;
    --bronze: #a0764a;
    --espresso: #3b2a1c;
    --stripe: #f6c796;
    --photo-dark: #33261d;
    --photo-mid: #6b4a33;
    --photo-wood: #a8703f;
    --photo-light: #c9c4bd;
  }
  * { margin: 0; padding: 0; box-sizing: border-box; }
  html, body {
    width: 840px;
    height: 1200px;
    overflow: hidden;
    background: var(--page);
  }
  .cover {
    position: absolute;
    left: 32px;
    top: 0;
    width: 776px;
    height: 1200px;
    overflow: hidden;
    background: radial-gradient(ellipse at 30% 35%, var(--cover-light) 0%, #f3f3f5 55%, var(--cover-shade) 100%);
  }
  .cover__art {
    position: absolute;
    inset: 0;
    width: 776px;
    height: 1200px;
  }
  .title-band__label,
  .title__bold,
  .byline {
    font-family: "Bebas Neue", "Oswald", sans-serif;
  }
  .title__thin {
    font-family: "Oswald", sans-serif;
    font-weight: 200;
  }
  .professor {
    position: absolute;
    left: 48px;
    top: 598px;
    width: 330px;
    height: 514px;
    border-radius: 46% 46% 30% 30% / 38% 38% 14% 14%;
    background:
      linear-gradient(180deg,
        #eef0f6 0%,
        #eef0f6 22%,
        #f8c98f 24%,
        #f8c98f 62%,
        #f4f5f9 64%,
        #f4f5f9 90%,
        #7a5636 92%,
        #7a5636 100%);
    opacity: 0.9;
  }
</style>
</head>
<body>
  <main class="cover">
    <svg class="cover__art" viewBox="0 0 776 1200" xmlns="http://www.w3.org/2000/svg" aria-label="Capital Area Property's Complete Handbook for Savvy Purchasers, by Marisa Vendrapolo and Jonathan Wexbrunel">
      <defs>
        <pattern id="stripes" width="5" height="10" patternUnits="userSpaceOnUse">
          <rect width="1.6" height="10" fill="var(--stripe)"/>
        </pattern>
        <linearGradient id="interior-photo-top" x1="0" y1="0" x2="0" y2="1">
          <stop offset="0" stop-color="var(--photo-light)"/>
          <stop offset="0.45" stop-color="var(--photo-mid)"/>
          <stop offset="1" stop-color="var(--photo-dark)"/>
        </linearGradient>
        <linearGradient id="interior-photo-floor" x1="0" y1="0" x2="0" y2="1">
          <stop offset="0" stop-color="var(--photo-dark)"/>
          <stop offset="0.5" stop-color="var(--photo-mid)"/>
          <stop offset="1" stop-color="var(--photo-wood)"/>
        </linearGradient>
      </defs>

      <!-- title band -->
      <g class="title-band">
        <rect x="319" y="93" width="92" height="38" fill="url(#stripes)"/>
        <rect x="413" y="93" width="4" height="38" fill="var(--stripe)"/>
        <text class="title-band__label" x="424" y="131" font-size="56" fill="var(--bronze)" textLength="210" lengthAdjust="spacingAndGlyphs">CAPITAL AREA</text>
        <rect x="641" y="93" width="4" height="38" fill="var(--stripe)"/>
        <rect x="648" y="93" width="64" height="38" fill="url(#stripes)"/>
      </g>

      <!-- main title -->
      <g class="title">
        <text class="title__thin" x="319" y="229" font-size="86" fill="var(--espresso)" textLength="388" lengthAdjust="spacingAndGlyphs">PROPERTY'S</text>
        <text class="title__bold" x="319" y="336" font-size="126" fill="url(#interior-photo-top)" textLength="394" lengthAdjust="spacingAndGlyphs" role="img" aria-label="Title word filled with a photo of a home interior">COMPLETE</text>
        <text class="title__bold" x="319" y="518" font-size="232" fill="url(#interior-photo-floor)" textLength="394" lengthAdjust="spacingAndGlyphs" role="img" aria-label="Title word filled with a photo of a kitchen with wood floors">HANDBOOK</text>
        <text class="title__thin" transform="translate(385 672) rotate(-90)" x="0" y="0" font-size="66" fill="var(--espresso)" textLength="68" lengthAdjust="spacingAndGlyphs">FOR</text>
        <text class="title__bold" x="399" y="692" font-size="153" fill="var(--bronze)" textLength="313" lengthAdjust="spacingAndGlyphs">SAVVY</text>
        <text class="title__bold" x="399" y="763" font-size="104" fill="var(--bronze)" textLength="308" lengthAdjust="spacingAndGlyphs">PURCHASERS</text>
      </g>

      <!-- byline -->
      <g class="byline" fill="var(--espresso)" font-size="31" text-anchor="end">
        <text x="705" y="951">BY MARISA VENDRAPOLO</text>
        <text x="705" y="985">AND JONATHAN WEXBRUNEL</text>
      </g>

      <!-- footer band -->
      <rect class="footer-band" x="450" y="1071" width="326" height="31" fill="url(#stripes)"/>
    </svg>

    <div class="professor" role="img" aria-label="Cartoon professor mascot in a white lab coat holding a pointer toward the title"></div>
  </main>
</body>
</html>
```